Legal firm website redesign

Existing site for Sydney CBD lawyer needs clean and professional redesign - http://penfoldlaw.com.au

The site will be viewed by a wide range of users: businesses, individuals, referral partners and other lawyers.

Please see the list of must haves for further details

Target Market(s)

Businesses, individuals, referral partners and other lawyers

Industry/Entity Type

Lawyer

Requirements
Must have
• Prominent display of phone number.
List of services down the left hand side of the site (5x services or so).
Search box in header.
Please use the greys and blues from the existing header.
New header must include the wording "Efficiency - Fulfillment - Integrity - Teamwork"

```html
<!DOCTYPE html>
<html lang="en">
<head>
<meta charset="utf-8">
<title>Penfold Law</title>
<link rel="stylesheet" href="https://fonts.googleapis.com/css2?family=Arimo:wght@400&display=swap">
<style>
:root{
  --header-dark:#2e2e2e;
  --header-light:#4a4a4a;
  --logo-grey:#c4c4c4;
  --tagline:#dcdcdc;
  --nav-top:#ffffff;
  --nav-bottom:#dcdcdc;
  --nav-text:#4a4a4a;
  --heading:#505050;
  --body:#333333;
  --muted:#5a5a5a;
  --rule:#8a8a8a;
  --link:#1b74c8;
  --box-top:#f4f4f4;
  --box-bottom:#e6e6e6;
  --hero-deep:#0e5f9c;
  --hero-mid:#2d93c9;
  --hero-light:#8fd3e6;
  --hero-green:#6fcf9a;
  --phone-blue:#2c9be0;
}
*{margin:0;padding:0;box-sizing:border-box}
html,body{width:1014px;height:1200px;overflow:hidden;background:#fff}
body{position:relative;font-family:"Arimo",Arial,sans-serif;color:var(--body)}
.site-header{position:absolute;left:0;top:0;width:1014px;height:288px;
  background:radial-gradient(ellipse 420px 260px at 60px 40px,var(--header-light),var(--header-dark) 75%),var(--header-dark)}
.brand{position:absolute;left:46px;top:40px;font-size:54px;color:var(--logo-grey);letter-spacing:1px;line-height:1}
.tagline{position:absolute;left:47px;top:106px;font-size:23px;color:var(--tagline);word-spacing:6px}
.search{position:absolute;left:796px;top:105px;width:186px;height:28px;border:1px solid #8a8a8a;background:#4c4c4c;
  color:#e8e8e8;font-size:14px;padding:5px 7px}
.search svg{position:absolute;right:6px;top:3px}
.main-nav{position:absolute;left:42px;top:171px;width:940px;height:56px;background:linear-gradient(var(--nav-top),var(--nav-bottom))}
.main-nav a{position:absolute;top:18px;font-size:20px;color:var(--nav-text);text-decoration:none}
.nav-phone{position:absolute;left:728px;top:14px;font-size:24px;color:var(--nav-text);display:flex;align-items:center;gap:9px}
.hero{position:absolute;left:42px;top:227px;width:940px;height:250px;
  background:linear-gradient(115deg,var(--hero-green) 0%,var(--hero-light) 22%,var(--hero-mid) 50%,var(--hero-deep) 78%,var(--hero-mid) 100%)}
.hero-word{position:absolute;left:748px;top:102px;font-size:37px;color:#fff;letter-spacing:1px}
h2{position:absolute;font-weight:400;color:var(--heading);line-height:1}
.services-title{left:42px;top:542px;font-size:29px}
.services{position:absolute;left:42px;top:603px;list-style:none;font-size:15px;line-height:18px;color:var(--muted)}
.divider-v{position:absolute;left:254px;top:552px;width:1px;height:193px;background:var(--rule)}
.about-title{left:298px;top:542px;font-size:29px}
.about{position:absolute;left:298px;top:601px;width:665px;font-size:13px;line-height:17px}
.about p{margin-bottom:16px}
.rule{position:absolute;left:42px;width:922px;height:1px;background:var(--rule)}
.commercial-title{left:40px;top:810px;font-size:27px}
.commercial{position:absolute;left:42px;top:863px;list-style:none;font-size:14px;line-height:17px}
.contact-card{position:absolute;left:43px;top:998px;width:437px;height:100px;background:linear-gradient(var(--box-top),var(--box-bottom))}
.contact-card .card-name{position:absolute;left:18px;top:32px;font-size:29px;color:var(--heading)}
.contact-card address{position:absolute;left:217px;top:6px;font-style:normal;font-size:16px;line-height:19px;color:var(--body)}
.recent-title{left:553px;top:810px;font-size:27px}
.recent{position:absolute;left:553px;top:863px;list-style:none;font-size:14px;line-height:17px}
.footer-copy{position:absolute;left:42px;top:1130px;font-size:13px;line-height:17px;color:var(--muted)}
.footer-nav a{position:absolute;top:1130px;font-size:14px;color:var(--link);text-decoration:none}
</style>
</head>
<body>
<header class="site-header">
  <div class="brand">penfold law</div>
  <div class="tagline">Efficiency Fulfillment Integrity Teamwork</div>
  <div class="search">Search...
    <svg width="26" height="22" viewBox="0 0 26 22"><circle cx="16" cy="8" r="6" fill="none" stroke="#eee" stroke-width="2"/><line x1="11.5" y1="12.5" x2="4" y2="19" stroke="#eee" stroke-width="3" stroke-linecap="round"/></svg>
  </div>
</header>
<nav class="main-nav">
  <a href="#" style="left:26px">Home</a>
  <a href="#" style="left:124px">About Us</a>
  <a href="#" style="left:245px">Areas Of Law</a>
  <a href="#" style="left:410px">Publications</a>
  <a href="#" style="left:563px">Contact</a>
  <div class="nav-phone">
    <svg width="26" height="26" viewBox="0 0 26 26"><circle cx="13" cy="13" r="12.5" fill="var(--phone-blue)"/><path d="M9 6.5c1 0 1.6 2.8 1.2 3.6l-1 1c.8 2 2.2 3.5 4.2 4.4l1-1c.8-.5 3.6.2 3.6 1.2 0 1.6-1.4 3-3 3C10 18.2 7 13.8 7 9c0-1.3 1-2.5 2-2.5z" fill="#fff"/></svg>
    <span>(02) 9000 4410</span>
  </div>
</nav>
<div class="hero" role="img" aria-label="Photograph of a modern glass building facade with diagonal blue and green reflections">
  <span class="hero-word">Diverse</span>
</div>

<h2 class="services-title">Services</h2>
<ul class="services">
  <li>Financing</li><li>Leading</li><li>Property Transactions</li><li>Join Ventures</li><li>Business Restructuring</li><li>Contract Review &amp; Advice</li>
</ul>
<div class="divider-v"></div>
<h2 class="about-title">About Penfold Law</h2>
<div class="about">
  <p>Penfold Law is a dynamic commercial law firm in the CBD of Sydney providing services to corporate, small business and private clients.</p>
  <p>Penfold Law brings together over 30 years of experience in legal practice.</p>
  <p>The strong focus of the firm is on commercial law and estate planning.</p>
  <p>Penfold Law is committed to providing quality legal services in helping its clients achieve their objectives by providing a proactive understanding of its clients' businesses and creative legal solutions.</p>
</div>
<div class="rule" style="top:779px"></div>

<h2 class="commercial-title">Commercial/Business Transactions</h2>
<ul class="commercial">
  <li>Buying and selling businesses and companies</li><li>Financing</li><li>Leasing</li><li>Property transactions</li><li>Business restructuring</li><li>Contract review and advice</li><li>Employment Law Documentation, e.g. AWAs</li>
</ul>
<div class="contact-card">
  <div class="card-name">penfold law</div>
  <address>Sydney NSW 2000<br>Telephone: (02) 9000 4410<br>Facsimile:&nbsp;&nbsp; (02) 9000 4420<br>info@penfoldlaw.com.au</address>
</div>

<h2 class="recent-title">Recent Additions</h2>
<ul class="recent">
  <li>Commencement of the Succession Act 2006 25.03.08</li>
  <li>Is that will valid? 15.01.08</li>
  <li>Labor's proposed changes to IR laws 14.12.07</li>
  <li>Should you make your own will? 14.11.07</li>
  <li>Illegal workers 14.08.07</li>
  <li>Employees' liability for misleading or deceptive conduct 14.08.07</li>
  <li>Correct use of ACNs and ABNs 14.08.07</li>
  <li>Power of Attorney Infosheet 10.08.07</li>
  <li>Intestate Estates Infosheet 08.08.07</li>
  <li>Estate Planning Infosheet 07.06.07</li>
  <li>Special Disability Trusts Infosheet 18.05.07</li>
  <li>Testamentary Trusts Infosheet 17.05.07</li>
  <li>Appointment of an Enduring Guardian Infosheet 15.05.07</li>
</ul>

<div class="rule" style="top:1118px"></div>
<footer>
  <div class="footer-copy">2012 penfold law<br>All rights &nbsp;reserved.</div>
  <nav class="footer-nav">
    <a href="#" style="left:536px">Home</a>
    <a href="#" style="left:604px">About Us</a>
    <a href="#" style="left:689px">Areas Of Law</a>
    <a href="#" style="left:805px">Publications</a>
    <a href="#" style="left:912px">Contact</a>
  </nav>
</footer>
</body>
</html>
```